Mental health agency needs an ad for brochure

Please provide us with a half page (W 8.5 inches x H 5.5 inches) advertising our company. We are a mental health agency that provides training, education, and consultation for companies that serve children, adolescents, or adults. We can offer training and education to help companies better serve their clientele and consultation about how companies are currently working with their staff or clientele. Our website is www.quellbrook.com and they can contact us at info@haverstoneinstitute.com or 503-847-2163.

```html
<!DOCTYPE html>
<html lang="en">
<head>
<meta charset="utf-8">
<title>Haverstone Institute – Half Page Ad</title>
<link href="https://fonts.googleapis.com/css2?family=Montserrat:wght@400;500;600&display=swap" rel="stylesheet">
<style>
  :root{
    --navy:#1a2d5a;
    --teal:#138cba;
    --white:#ffffff;
    --backdrop:#d9d9d9;
  }
  *{margin:0;padding:0;box-sizing:border-box}
  html,body{width:1200px;height:1200px;overflow:hidden;background:var(--backdrop);font-family:'Montserrat',sans-serif}
  .ad{position:absolute;left:50px;top:244px;width:1559px;height:1008px;transform:scale(0.70558);transform-origin:0 0;background:var(--teal);overflow:hidden}
  .ad-shapes{position:absolute;inset:0}
  .brand{position:absolute;left:100px;top:70px;width:400px;text-align:center;color:var(--navy);font-weight:500;font-size:27px;line-height:34px;letter-spacing:1px;text-transform:uppercase}
  .brand-mark{width:130px;height:130px;border-radius:50%;background:var(--navy);margin:0 auto 26px}
  .headline{position:absolute;left:48px;top:352px;color:var(--white);font-weight:600;font-size:46px;line-height:54px;white-space:nowrap}
  .rule{position:absolute;left:45px;width:690px;height:2px;background:var(--white)}
  .rule-accent{position:absolute;left:20px;top:-2px;width:85px;height:6px;background:var(--teal)}
  .bullets{position:absolute;left:46px;top:504px;width:720px;list-style:none;color:var(--white);font-size:23.6px;line-height:28px;letter-spacing:.6px;white-space:nowrap}
  .bullets li{position:relative;padding-left:36px;margin-bottom:17px}
  .bullets svg{position:absolute;left:0;top:4px}
  .contact{position:absolute;left:45px;display:flex;align-items:center;color:var(--navy);white-space:nowrap}
  .contact svg{flex:none;margin-right:16px}
  .contact-phone{top:790px;font-size:42px;font-weight:600;letter-spacing:1px}
  .contact-line{top:848px;background:var(--teal)}
  .contact-email{top:862px;font-size:30px;letter-spacing:1.5px}
  .contact-web{top:918px;font-size:30px;letter-spacing:1.5px}
  .photo{position:absolute;left:779px;width:289px;height:288px;border:7px solid var(--white);box-shadow:0 2px 8px rgba(0,0,0,.2)}
  .photo-1{top:46px;background:linear-gradient(135deg,#d8d3cc,#8f7a66 55%,#3b3b3b)}
  .photo-2{top:360px;background:linear-gradient(135deg,#b98a5a,#e8d07c 50%,#f0c2c4)}
  .photo-3{top:674px;background:linear-gradient(135deg,#e4e6e8,#c5c9cf 50%,#4d6f9c)}
  .provide{position:absolute;left:1112px;top:0;width:402px;color:var(--white)}
  .provide-title{position:absolute;left:2px;top:38px;font-size:36px;font-weight:600;letter-spacing:.5px;white-space:nowrap}
  .provide-line{position:absolute;left:0;width:402px;height:2px;background:var(--white)}
  .provide-accent{position:absolute;left:20px;top:-3px;width:85px;height:6px;background:var(--navy)}
  .provide-text{position:absolute;left:2px;width:400px;font-size:24px;line-height:29px;letter-spacing:.7px;white-space:nowrap}
</style>
</head>
<body>
<div class="ad">
  <svg class="ad-shapes" width="1559" height="1008" viewBox="0 0 1559 1008">
    <polygon points="644,0 696,0 779,172 779,200" fill="#1a2d5a"/>
    <polygon points="779,810 779,840 696,1008 644,1008" fill="#1a2d5a"/>
    <polygon points="0,0 644,0 779,179 779,824 644,1008 0,1008" fill="#ffffff"/>
    <polygon points="0,46 47,46 146,162 47,279 0,279" fill="#138cba"/>
    <rect x="0" y="325" width="779" height="421" fill="#1a2d5a"/>
  </svg>

  <div class="brand">
    <div class="brand-mark"></div>
    Haverstone Institute<br>Northwest, LLC
  </div>

  <h1 class="headline">Nurture Authentic and Safe<br>Relationships Around You</h1>
  <div class="rule" style="top:477px"><span class="rule-accent"></span></div>

  <ul class="bullets">
    <li><svg width="22" height="22" viewBox="0 0 22 22"><circle cx="11" cy="11" r="11" fill="#138cba"/><path d="M6 11.5l3.2 3L16 8" stroke="#fff" stroke-width="2.4" fill="none" stroke-linecap="round" stroke-linejoin="round"/></svg>We are a mental health agency that provides<br>training, education, and consultation for companies<br>that serve children, adolescents, or adults.</li>
    <li><svg width="22" height="22" viewBox="0 0 22 22"><circle cx="11" cy="11" r="11" fill="#138cba"/><path d="M6 11.5l3.2 3L16 8" stroke="#fff" stroke-width="2.4" fill="none" stroke-linecap="round" stroke-linejoin="round"/></svg>We can offer training and education to help<br>companies better serve their clientele &amp; consultation<br>about how companies are currently working with<br>their staff or clientele.</li>
  </ul>

  <div class="contact contact-phone">
    <svg width="44" height="44" viewBox="0 0 44 44"><circle cx="22" cy="22" r="22" fill="#138cba"/><path d="M15 12c1.5-1 2.5 0 3.5 2l1.3 2.6c.5 1.2 0 2-1 2.7l-1 .7c.8 2.6 2.8 4.8 5.4 5.9l.8-1c.8-1 1.6-1.3 2.7-.7l2.6 1.4c1.800 1 2.6 2 1.5 3.5-1.5 2-3.5 2.6-6 1.6-5.2-2.1-9.1-6.3-10.8-11.5-.8-2.5-.4-5 1-7.2z" fill="none" stroke="#fff" stroke-width="1.8"/></svg>
    <span>503-847-2163</span>
  </div>
  <div class="rule contact-line"></div>
  <div class="contact contact-email">
    <svg width="44" height="44" viewBox="0 0 44 44"><circle cx="22" cy="22" r="22" fill="#138cba"/><rect x="11" y="14" width="22" height="16" rx="1.5" fill="none" stroke="#fff" stroke-width="1.8"/><path d="M11 15l11 8 11-8M11 29l8-7M33 29l-8-7" fill="none" stroke="#fff" stroke-width="1.6"/></svg>
    <span>info@haverstoneinstitute.com</span>
  </div>
  <div class="contact contact-web">
    <svg width="44" height="44" viewBox="0 0 44 44"><circle cx="22" cy="22" r="22" fill="#138cba"/><g fill="none" stroke="#fff" stroke-width="1.7"><circle cx="22" cy="22" r="12"/><ellipse cx="22" cy="22" rx="5.5" ry="12"/><path d="M10 22h24M12 16h20M12 28h20"/></g></svg>
    <span>www.quellbrook.com</span>
  </div>

  <div class="photo photo-1" role="img" aria-label="Photo: a counselor listening to a distressed woman in a therapy room"></div>
  <div class="photo photo-2" role="img" aria-label="Photo: a smiling woman and a young girl playing a learning game at a table"></div>
  <div class="photo photo-3" role="img" aria-label="Photo: a therapist with a clipboard talking with a client on a sofa"></div>

  <section class="provide">
    <h2 class="provide-title">WHAT WE PROVIDE</h2>
    <div class="provide-line" style="top:86px"><span class="provide-accent"></span></div>
    <p class="provide-text" style="top:127px">Reduce stress and develop<br>poise in managing behaviors<br>in your school and non-profit<br>child-serving organizations<br>with training in the area of<br>trauma and its effect on the<br>brain and body.</p>
    <div class="provide-line" style="top:359px"></div>
    <p class="provide-text" style="top:403px">Develop confidence and<br>become self-assured to build<br>strong &amp; reliable boundaries in<br>relationship with others using<br>body-oriented therapy, offered<br>for individuals, couples, and<br>families.</p>
    <div class="provide-line" style="top:672px"></div>
    <p class="provide-text" style="top:714px">Decrease staff stress, burnout,<br>and absenteeism while<br>increasing staff authenticity<br>and openness using feedback<br>and heatmapping tools across<br>teams and departments in<br>your organization.</p>
    <div class="provide-line" style="top:960px"></div>
  </section>
</div>
</body>
</html>
```